Stonebrook Business Card Redesign & Logo Update

We need to update our business cards to something more modern and fresh. Stonebrook can provide the current color schemes and old design examples, but welcome creativity in helping us with this redesign. PLEASE NOTE that we no longer utilize the "tree" and/or "leaf" imagery in our branding. If able would apprecaite an update on the quality of our "words only" logo in Ai. / PNG formats too.

Target Market(s)

Investors, landowners, corporate partners, contractors

Industry/Entity Type

Environmental Restoration & Conservation

Contact Information for Business Card

Logo, persons name, title, mailing address, phone and email, website url

Font styles to use
Other font styles liked:
• Merriweather

Requirements
Nice to have
• Logo, persons name, title, mailing address, phone and email, website url, but open to ideams
Should not have
• No all back backgrounds

```html
<!DOCTYPE html>
<html lang="en">
<head>
<meta charset="utf-8">
<title>Stonebrook Business Cards</title>
<link rel="stylesheet" href="https://fonts.googleapis.com/css2?family=Merriweather:wght@400;700;900&display=swap">
<style>
  :root {
    --bg: #e9ecea;
    --card: #ffffff;
    --green-dark: #1f7a2e;
    --green-mid: #3a9a35;
    --green-light: #8cc63f;
    --ink: #1d1d1d;
    --ink-soft: #444444;
    --icon-dark: #1f3322;
    --icon-grey: #6d6d6d;
  }
  * { margin: 0; padding: 0; box-sizing: border-box; }
  html, body {
    width: 1200px; height: 780px; overflow: hidden;
    background: var(--bg);
    font-family: "Merriweather", Georgia, serif;
  }
  .canvas { position: relative; width: 1200px; height: 780px; }
  .card {
    position: absolute;
    width: 540px; height: 310px;
    background: var(--card);
    border-radius: 18px;
    box-shadow: 0 6px 18px rgba(0,0,0,0.12);
    overflow: hidden;
  }
  /* Front */
  .card-front { left: 60px; top: 390px; }
  .front-artwork {
    position: absolute; left: 0; top: 0;
    width: 240px; height: 190px;
    background: radial-gradient(ellipse at 20% 70%, var(--green-dark) 0%, var(--green-mid) 45%, rgba(140,198,63,0.55) 75%, rgba(255,255,255,0) 100%);
    border-bottom-right-radius: 120px;
  }
  .front-logo {
    position: absolute; left: 210px; top: 150px;
    font-size: 44px; font-weight: 900;
    color: var(--green-dark);
    letter-spacing: 0.5px;
  }
  .front-web {
    position: absolute; left: 214px; top: 218px;
    font-size: 15px; color: var(--green-dark);
  }
  /* Back */
  .card-back { left: 600px; top: 80px; }
  .back-logo {
    position: absolute; left: 28px; top: 52px;
    font-size: 30px; font-weight: 900;
    color: var(--green-dark);
  }
  .contact-list {
    position: absolute; left: 200px; top: 120px;
    list-style: none;
  }
  .contact-item {
    display: flex; align-items: flex-start; gap: 12px;
    margin-bottom: 10px;
  }
  .contact-icon {
    flex: 0 0 26px; width: 26px; height: 26px;
    border-radius: 50%;
    display: flex; align-items: center; justify-content: center;
  }
  .contact-icon.dark { background: var(--icon-dark); }
  .contact-icon.grey { background: var(--icon-grey); }
  .contact-icon svg { width: 14px; height: 14px; }
  .person-name {
    font-size: 17px; font-weight: 900; color: var(--ink);
    letter-spacing: 1px; line-height: 1.1;
  }
  .person-title {
    font-size: 10px; color: var(--ink-soft); letter-spacing: 1px;
  }
  .contact-text {
    font-size: 11.5px; color: var(--ink); line-height: 1.45;
  }
</style>
</head>
<body>
<main class="canvas">

  <section class="card card-back" aria-label="Business card back">
    <div class="back-logo">Stonebrook</div>
    <ul class="contact-list">
      <li class="contact-item">
        <span class="contact-icon dark">
          <svg viewBox="0 0 16 16"><circle cx="8" cy="5" r="3" fill="#fff"/><path d="M2.5 15c0-3.5 2.5-5.5 5.5-5.5s5.5 2 5.5 5.5z" fill="#fff"/></svg>
        </span>
        <div>
          <div class="person-name">DANIEL MARSH</div>
          <div class="person-title">FOUNDER</div>
        </div>
      </li>
      <li class="contact-item">
        <span class="contact-icon grey">
          <svg viewBox="0 0 16 16"><path d="M4 1.5l2.5 3-1.5 1.8c.8 1.7 2 2.9 3.7 3.7L10.5 8.5l3 2.5-1.3 2.6C6.5 13.5 2.5 9.5 1.5 3.3z" fill="#fff"/></svg>
        </span>
        <div class="contact-text">+000 55512 3400<br>+000 55512 3401</div>
      </li>
      <li class="contact-item">
        <span class="contact-icon grey">
          <svg viewBox="0 0 16 16" fill="none" stroke="#fff" stroke-width="1.3"><circle cx="8" cy="8" r="6"/><ellipse cx="8" cy="8" rx="2.6" ry="6"/><line x1="2" y1="8" x2="14" y2="8"/></svg>
        </span>
        <div class="contact-text">www.stonebrookrestore.com<br>info@stonebrookrestore.com</div>
      </li>
      <li class="contact-item">
        <span class="contact-icon dark">
          <svg viewBox="0 0 16 16"><path d="M8 1a5 5 0 0 1 5 5c0 3.5-5 9-5 9S3 9.5 3 6a5 5 0 0 1 5-5z" fill="#fff"/><circle cx="8" cy="6" r="1.8" fill="#1f3322"/></svg>
        </span>
        <div class="contact-text">48 Millrace Road,<br>Riverton</div>
      </li>
    </ul>
  </section>

  <section class="card card-front" aria-label="Business card front">
    <div class="front-artwork" role="img" aria-label="Green branch and leaf illustration in the top left corner"></div>
    <div class="front-logo">Stonebrook</div>
    <div class="front-web">www.stonebrookrestore.com</div>
  </section>

</main>
</body>
</html>
```